Finance Company Need Presentation Folder/ Brochure Design

We are a Finance Brokerage Firm in Adelaide, we provide finance for personal, car, equipment, boat and aviation loans. We are looking for designs for new presentation folders that are simplistic, yet professional and classy. We would like them to include the color orange and communicate financial safety and growth.

Target Market(s)

The folders will be going to current and perspective clients

Industry/Entity Type

Finance

Font styles to use
Other font styles liked:
• Raleway or something similar, example attached as 'Open Door Lending Evening'

Colors
f37122
ffffff
000000

Requirements
Must have
• Phone Number: 1300 482 917
• Address:
• 47 Tamsin Road
• Brindlemoor, SA 5092
• Website: kelvarupath.com.au
Nice to have
• "Experience finance in a whole new way... Experience Kelvarupath"
• Asset Finance - Home Loans - Personal Loans

```html
<!DOCTYPE html>
<html lang="en">
<head>
<meta charset="utf-8">
<title>Kelvarupath Presentation Folder</title>
<link rel="stylesheet" href="https://fonts.googleapis.com/css2?family=Raleway:wght@300;400;600;700&display=swap">
<style>
  :root {
    --orange: #cf5128;
    --orange-light: #e35e2c;
    --charcoal: #2c2c2c;
    --charcoal-light: #595959;
    --white: #ffffff;
    --ink: #333333;
    --brand-ink: #3a3a3a;
    --card-slot: #f3b08d;
    --backdrop: #d2d2d2;
    --spine-shade: #ececec;
  }
  * { margin: 0; padding: 0; box-sizing: border-box; }
  html, body {
    width: 1200px; height: 2270px; overflow: hidden;
    background: linear-gradient(180deg, #c9c9c9 0%, var(--backdrop) 40%, #d6d6d6 100%);
    font-family: 'Raleway', sans-serif;
  }
  .spread {
    position: absolute; left: 100px; width: 1000px; height: 707px;
    box-shadow: 0 30px 50px rgba(0,0,0,0.22);
    overflow: hidden;
  }
  .outer-spread { top: 220px; background: var(--orange); }
  .inner-spread { top: 1260px; background: var(--white); }

  .panel { position: absolute; top: 0; width: 500px; height: 707px; }
  .panel-back { left: 0; }
  .panel-front { left: 500px; }
  .spine-fold {
    position: absolute; left: 0; top: 0; width: 60px; height: 100%;
    background: linear-gradient(90deg, rgba(0,0,0,0.12), rgba(0,0,0,0));
  }

  /* decorative artwork areas */
  .cover-artwork { position: absolute; left: 0; width: 500px; }
  .panel-back .cover-artwork {
    top: 470px; height: 237px;
    background: linear-gradient(170deg, var(--orange) 0%, var(--charcoal) 55%, var(--charcoal-light) 100%);
  }
  .panel-front .cover-artwork {
    top: 450px; height: 257px;
    background: linear-gradient(160deg, var(--orange) 0%, var(--charcoal) 60%, var(--charcoal-light) 100%);
  }

  /* back cover contact block */
  .contact-block {
    position: absolute; left: 0; top: 120px; width: 500px;
    text-align: center; color: var(--white);
  }
  .contact-block .brand-name {
    font-weight: 400; font-size: 30px; color: var(--brand-ink); letter-spacing: 0.5px;
    margin-bottom: 34px;
  }
  .contact-item { font-size: 16px; font-weight: 400; line-height: 1.35; margin-bottom: 16px; }
  .contact-item svg { display: block; margin: 0 auto 6px; width: 16px; height: 16px; }

  /* front cover */
  .cover-message { position: absolute; left: 45px; top: 190px; width: 430px; }
  .cover-message .lead { color: var(--white); font-weight: 700; font-size: 36px; line-height: 1.1; }
  .cover-message .sub { color: var(--white); font-weight: 400; font-size: 25px; line-height: 1.25; }
  .cover-message .closing { color: var(--ink); font-weight: 700; font-size: 33px; line-height: 1.15; }
  .cover-message .brand-name { color: var(--white); font-weight: 300; font-size: 40px; margin-top: 28px; }

  /* inner pockets */
  .inner-spread svg { position: absolute; inset: 0; display: block; }
  .pocket-brand {
    position: absolute; left: 60px; top: 575px;
    color: var(--white); font-weight: 300; font-size: 50px;
  }
  .card-slot-label {
    position: absolute; left: 740px; top: 537px; width: 170px; height: 115px;
    display: flex; align-items: center; justify-content: center; text-align: center;
    color: var(--ink); font-size: 17px; font-weight: 400; line-height: 1.25;
  }
</style>
</head>
<body>

<section class="spread outer-spread" aria-label="Folder outside: back and front cover">
  <div class="panel panel-back">
    <div class="cover-artwork" role="img" aria-label="Decorative cover artwork in orange and charcoal"></div>
    <div class="contact-block">
      <p class="brand-name">Kelvarupath</p>
      <div class="contact-item">
        <svg viewBox="0 0 16 16" aria-hidden="true"><path d="M4 1.5l2.2 3-1.3 1.6c.8 1.9 2.2 3.3 4 4.1l1.6-1.3 3 2.2-1.2 2.4C7.4 13.3 2.7 8.6 1.7 2.7z" fill="#3a3a3a"/></svg>
        1300 482 917
      </div>
      <div class="contact-item">
        <svg viewBox="0 0 16 16" aria-hidden="true"><path d="M8 1a4.5 4.5 0 0 0-4.5 4.5C3.5 9 8 15 8 15s4.5-6 4.5-9.5A4.5 4.5 0 0 0 8 1zm0 6.3a1.8 1.8 0 1 1 0-3.6 1.8 1.8 0 0 1 0 3.6z" fill="#3a3a3a"/></svg>
        47 Tamsin Road<br>Brindlemoor, SA 5092
      </div>
      <div class="contact-item">
        <svg viewBox="0 0 16 16" aria-hidden="true"><circle cx="8" cy="8" r="6.5" fill="none" stroke="#3a3a3a" stroke-width="1.6"/><path d="M1.5 8h13M8 1.5c2.2 2 2.2 11 0 13M8 1.5c-2.2 2-2.2 11 0 13" fill="none" stroke="#3a3a3a" stroke-width="1.2"/></svg>
        kelvarupath.com.au
      </div>
    </div>
  </div>

  <div class="panel panel-front">
    <div class="cover-artwork" role="img" aria-label="Decorative cover artwork in orange and charcoal"></div>
    <div class="spine-fold"></div>
    <div class="cover-message">
      <p class="lead">Experience finance</p>
      <p class="sub">in a whole new way...</p>
      <p class="closing">Experience Kelvarupath</p>
      <p class="brand-name">Kelvarupath</p>
    </div>
  </div>
</section>

<section class="spread inner-spread" aria-label="Folder inside with two pockets">
  <svg viewBox="0 0 1000 707" width="1000" height="707" aria-hidden="true">
    <defs>
      <linearGradient id="inner-spine" x1="0" y1="0" x2="1" y2="0">
        <stop offset="0" stop-color="var(--spine-shade)"/>
        <stop offset="1" stop-color="#ffffff"/>
      </linearGradient>
      <linearGradient id="pocket-glow" x1="0" y1="0" x2="1" y2="0">
        <stop offset="0" stop-color="var(--orange)"/>
        <stop offset="0.5" stop-color="var(--orange-light)"/>
        <stop offset="1" stop-color="var(--orange)"/>
      </linearGradient>
    </defs>
    <rect x="500" y="0" width="90" height="707" fill="url(#inner-spine)"/>
    <path class="pocket-left" d="M0 470 H440 Q470 470 472 500 L492 707 H0 Z" fill="url(#pocket-glow)"/>
    <path class="pocket-right" d="M508 707 L528 500 Q530 470 560 470 H1000 V707 Z" fill="url(#pocket-glow)"/>
    <polygon class="card-slot" points="752,537 898,537 910,552 910,637 898,652 752,652 740,637 740,552" fill="var(--card-slot)"/>
  </svg>
  <p class="pocket-brand">Kelvarupath</p>
  <p class="card-slot-label">Space for<br>Business card</p>
</section>

</body>
</html>
```